Webbanner-Design für online Folienballonshop
Zielgruppe
Wir werden in kürze mit einem Folienballonshop online gehen.
Aufgabenstellung
Wir brauchen ein Headerbanner für unseren neuen Online Shop. Hier ein Link zum Testshop, in dem Sie auch unser Logo finden: http://luftfest.vrx41.probehost-web.ch/
Der Name des Online Shops ist www.luftfest.ch
Wir benötigen die Headerbanner-Masse wie bei folgendem Link: https://muro.kel52.biz/. (So wird unsere neue Struktur)
In unseren Vorstellungen sollten verschiedene Folienballone im Einklang mit den 4 Jahreszeiten dargestellt werden.
Beispiele:
Im Winter ein Schneemann mit passenden Folienballone wie z.Bsp. http://luftfest.vrx41.probehost-web.ch/search?p=1&q=weihnachten&o=7&n=12&cf=7
Im Frühling ein Geburtstagsfest mit passenden Folienballone wie z.Bsp. http://luftfest.vrx41.probehost-web.ch/ungefuellt/anlass/geburtstag/?p=1
Im Sommer ein Hochzeitsauto mit passenden Folienballone wie z.Bsp. http://luftfest.vrx41.probehost-web.ch/ungefuellt/anlass/hochzeit/?p=1
Im Herbst ein Kürbis mit passenden Folienballone wie z.Bsp. http://luftfest.vrx41.probehost-web.ch/ungefuellt/anlass/helloween/
Das Bild sollte selber gestaltet und nicht mit gekauften Bildern umgesetzt werden.

```html
<!DOCTYPE html>
<html lang="de">
<head>
<meta charset="utf-8">
<title>Luftfest – Folienballone</title>
<link href="https://fonts.googleapis.com/css2?family=Open+Sans:wght@400;600&family=Jost:wght@400&display=swap" rel="stylesheet">
<style>
  :root{
    --page-bg:#ffffff;
    --text:#333b44;
    --muted:#8a9099;
    --line:#dcdfe3;
    --usp-bg:#eef0f4;
    --accent:#e8613a;
    --claim-bg:#2aa7dc;
    --claim-text:#ffffff;
    --footer-bg:#e8e8e8;
    --ink:#111111;
  }
  *{box-sizing:border-box;margin:0;padding:0}
  html,body{width:1200px;height:902px;overflow:hidden;background:var(--page-bg)}
  body{font-family:"Open Sans",Arial,sans-serif;color:var(--text);position:relative}

  .shop-page{position:absolute;left:0;top:160px;width:1200px;height:564px;overflow:hidden;
    box-shadow:0 0 14px rgba(0,0,0,.35);background:var(--page-bg)}

  .site-header{height:42px;position:relative;border-bottom:1px solid var(--line)}
  .brand{position:absolute;left:31px;top:6px;font-size:26px;font-weight:600;color:var(--text);letter-spacing:-.5px}
  .search{position:absolute;left:367px;top:5px;width:479px;height:31px;border:1px solid var(--line);
    font-size:10px;color:var(--muted);padding:9px 12px}
  .search svg{position:absolute;right:14px;top:7px}
  .header-actions{position:absolute;right:36px;top:11px;display:flex;gap:15px}

  .main-nav{height:36px;display:flex;justify-content:center;gap:18px;font-size:10px;border-bottom:1px solid var(--line)}
  .main-nav a{color:var(--text);text-decoration:none;line-height:34px;padding:0 6px;border-bottom:2px solid transparent}
  .main-nav a.is-active{border-bottom-color:var(--accent)}

  .usp-bar{height:32px;background:var(--usp-bg);position:relative;font-size:9.5px}
  .usp-bar ul{list-style:none;position:absolute;top:9px;left:0;width:100%}
  .usp-bar li{position:absolute;display:flex;align-items:center;gap:6px}
  .usp-close{position:absolute;right:41px;top:9px}

  .hero{height:373px;position:relative;
    background:
      radial-gradient(circle at 8% 10%,#f4d21c 0 6%,transparent 7%),
      radial-gradient(circle at 12% 45%,#3f8fd6 0 11%,transparent 12%),
      radial-gradient(circle at 33% 35%,#d83a3a 0 13%,transparent 14%),
      radial-gradient(circle at 41% 62%,#e7862a 0 10%,transparent 11%),
      radial-gradient(circle at 52% 80%,#f4d21c 0 8%,transparent 9%),
      radial-gradient(circle at 67% 45%,#f2f2f2 0 13%,transparent 14%),
      radial-gradient(circle at 87% 68%,#e8d3ae 0 10%,transparent 11%),
      linear-gradient(90deg,#dfe9f7 0%,#f7c9dc 40%,#fbe1e6 70%,#f6e9b4 100%)}
  .claims{position:absolute;right:12px;top:24px;display:flex;flex-direction:column;align-items:flex-end;gap:15px}
  .claim{font-family:"Jost",Arial,sans-serif;font-size:23px;color:var(--claim-text);background:var(--claim-bg);
    border:2px solid #fff;height:46px;line-height:42px;padding:0 9px;white-space:nowrap}

  .site-footer{height:81px;background:var(--footer-bg);position:relative;font-size:9.5px}
  .newsletter-icon{position:absolute;left:214px;top:27px;width:30px;height:30px;border-radius:50%;background:var(--ink)}
  .newsletter-icon svg{position:absolute;left:8px;top:9px}
  .newsletter-title{position:absolute;left:264px;top:34px;font-size:12px}
  .newsletter-field{position:absolute;left:215px;top:62px;width:355px;height:30px;background:#fff;border:1px solid var(--line);
    color:var(--muted);font-size:9px;padding:8px 6px}
  .footer-usp{position:absolute;left:596px;top:46px;list-style:none}
  .footer-usp li{display:flex;align-items:center;gap:6px;margin-bottom:6px}
</style>
</head>
<body>
<div class="shop-page">
  <header class="site-header">
    <div class="brand">Luftfest</div>
    <div class="search">Suchbegriff...
      <svg width="16" height="16" viewBox="0 0 16 16" fill="none" stroke="#555" stroke-width="1.4"><circle cx="6.5" cy="6.5" r="5"/><path d="M10.3 10.3 15 15"/></svg>
    </div>
    <div class="header-actions">
      <svg width="18" height="18" viewBox="0 0 18 18" fill="none" stroke="#333" stroke-width="1.4"><path d="M9 15.5 2.4 9A3.8 3.8 0 0 1 9 4a3.8 3.8 0 0 1 6.6 5z"/></svg>
      <svg width="18" height="18" viewBox="0 0 18 18" fill="none" stroke="#333" stroke-width="1.4"><circle cx="9" cy="9" r="7.3"/><circle cx="9" cy="7.3" r="2.5"/><path d="M4.5 14.3c1-2.3 2.6-3.2 4.5-3.2s3.5.9 4.5 3.2"/></svg>
      <svg width="18" height="18" viewBox="0 0 18 18" fill="none" stroke="#333" stroke-width="1.4"><path d="M1 2h2.5l2 9h8.5l1.8-6.5H4.4"/><circle cx="7" cy="15" r="1.2"/><circle cx="13" cy="15" r="1.2"/></svg>
    </div>
  </header>

  <nav class="main-nav">
    <a class="is-active" href="#">Home</a>
    <a href="#">Ungefüllt</a>
    <a href="#">Als Geschenk</a>
    <a href="#">Mit Heliumdose</a>
  </nav>

  <div class="usp-bar">
    <ul>
      <li style="left:241px"><svg width="13" height="13" viewBox="0 0 13 13" fill="none" stroke="#555"><circle cx="6.5" cy="6.5" r="5.8"/><path d="m3.8 6.7 1.9 1.9 3.6-3.8"/></svg>Kauf auf Rechnung</li>
      <li style="left:402px"><svg width="13" height="13" viewBox="0 0 13 13" fill="none" stroke="#555"><circle cx="6.5" cy="6.5" r="5.8"/><path d="m3.8 6.7 1.9 1.9 3.6-3.8"/></svg>Kostenloser Versand &amp; Rückversand</li>
      <li style="left:626px"><svg width="13" height="13" viewBox="0 0 13 13" fill="none" stroke="#555"><circle cx="6.5" cy="6.5" r="5.8"/><path d="m3.8 6.7 1.9 1.9 3.6-3.8"/></svg>1-3 Werktage Lieferzeit</li>
      <li style="left:820px"><svg width="13" height="13" viewBox="0 0 13 13" fill="none" stroke="#555"><circle cx="6.5" cy="6.5" r="5.8"/><path d="m3.8 6.7 1.9 1.9 3.6-3.8"/></svg>100 Tage Rückgaberecht</li>
    </ul>
    <svg class="usp-close" width="12" height="12" viewBox="0 0 12 12" stroke="#333" stroke-width="1.4"><path d="M2 2l8 8M10 2l-8 8"/></svg>
  </div>

  <section class="hero" role="img" aria-label="Bunte Folienballone für jeden Anlass: Schneemann, Zuckerstange, Herz, Kürbis, Brautkleid, Anzug, Geburtstagsballon und Hund vor rosa Lichthintergrund">
    <div class="claims">
      <div class="claim">Für jeden Anlass das Passende!</div>
      <div class="claim">Mehr als 200 Motive!</div>
      <div class="claim">Auch im Geschenkkarton buchbar!</div>
    </div>
  </section>

  <footer class="site-footer">
    <div class="newsletter-icon"><svg width="14" height="11" viewBox="0 0 14 11" fill="none" stroke="#fff" stroke-width="1.2"><rect x=".6" y=".6" width="12.8" height="9.8"/><path d="m.6.6 6.4 5.4L13.4.6"/></svg></div>
    <div class="newsletter-title">Newsletter</div>
    <div class="newsletter-field">Ihre E-Mail-Adresse</div>
    <ul class="footer-usp">
      <li><svg width="13" height="13" viewBox="0 0 13 13" fill="none" stroke="#555"><circle cx="6.5" cy="6.5" r="5.8"/><path d="m3.8 6.7 1.9 1.9 3.6-3.8"/></svg>Kauf auf Rechnung</li>
      <li><svg width="13" height="13" viewBox="0 0 13 13" fill="none" stroke="#555"><circle cx="6.5" cy="6.5" r="5.8"/><path d="m3.8 6.7 1.9 1.9 3.6-3.8"/></svg>Kostenloser Versand &amp; Rückversand</li>
    </ul>
  </footer>
</div>
</body>
</html>
```